Business Card Design for Pastor/Church Leadership - simple, elegant, "different"

Design a name card based on logo and color from our branding guide - see file "MBF Logo and Color".
The teal frame around the logo is not part of the logo and is a not necessary design element for the name card (as the attached PDF file may suggest).
The font suggested by branding is "Frutiger 55 Roman".
The file "not good.pdf", a sample of a name card that is NOT good.
- fonts too small to read
- the tagline on the logo "Still waters, open door" not easy to read with logo used in this design
- "MAPLE GROVE FELLOWSHIP" unnecessarily duplicated - possibly because logo too small
- not sure about the green frame, probably better to drop

Target Market(s)

broad, all people the pastor of an international church in Tokyo meets

Industry/Entity Type

Business

Contact Information for Business Card

Mattias R. Pellworth
Pastor
3-9-4 Kawaranodai, Kaede-ku
Tokyo 164-0012 (Church)
2-21 Ochibamachi, Kaede-ku
Tokyo 164-0027 (Home)
Tel: 03-5817-2963
E-mail: pastor@maplegrovefell.org
URL: http://www.maplegrovefell.org

Font styles to use
Sans Serif
Other font styles liked:
• Frutiger 55 Roman (want, not must)

Requirements
Must have
• must include logo
• must make use of the "bright turquoise color"
• Cyan = 59, Magenta = 0, Yellow=24, Black=0
• Red=3.1%, Green=91%, Blue=87.1%
• Key Info (name) must be easy to read (see notes on bad sample namecard attached)

```html
<!DOCTYPE html>
<html lang="en">
<head>
<meta charset="utf-8">
<title>Maple Grove Fellowship – Pastor Business Card</title>
<link rel="stylesheet" href="https://fonts.googleapis.com/css2?family=Noto+Sans:wght@400;500&display=swap">
<style>
  :root {
    --backdrop: #f7b95c;
    --card-white: #ffffff;
    --teal: #5bc5c7;
    --teal-mark: #4dbfbd;
    --ink: #111111;
    --rule: #1a1a1a;
    --on-teal: #ffffff;
  }
  * { box-sizing: border-box; margin: 0; padding: 0; }
  html, body {
    width: 1200px; height: 786px; overflow: hidden;
    background: var(--backdrop);
    font-family: "Noto Sans", "Helvetica Neue", Arial, sans-serif;
  }
  .stage {
    width: 1200px; height: 786px;
    display: flex; align-items: center; justify-content: center;
  }
  .business-card {
    position: relative;
    width: 900px; height: 545px;
    background: var(--card-white);
    box-shadow: 0 10px 30px rgba(120, 70, 0, 0.25);
    overflow: hidden;
  }
  .divider {
    position: absolute; left: 0; top: 330px; width: 100%; height: 4px;
    background: var(--rule);
  }
  .card-band {
    position: absolute; left: 0; top: 334px; width: 100%; height: 211px;
    background: var(--teal);
  }

  .brand {
    position: absolute; left: 60px; top: 110px; width: 330px;
    color: var(--teal-mark);
  }
  .brand-dot {
    display: block; width: 64px; height: 64px; border-radius: 50%;
    background: var(--teal-mark); margin: 0 0 18px 120px;
  }
  .brand-name {
    font-size: 17px; font-weight: 400; letter-spacing: 0.08em;
    white-space: nowrap;
    padding-bottom: 8px;
    border-bottom: 2px solid var(--teal-mark);
  }
  .brand-tagline {
    margin-top: 8px; font-size: 17px; letter-spacing: 0.04em;
    white-space: nowrap;
    padding-bottom: 8px;
    border-bottom: 2px solid var(--teal-mark);
  }

  .addresses {
    position: absolute; left: 430px; top: 180px;
    list-style: none; color: var(--ink);
    font-size: 25px; line-height: 1.22;
  }
  .address { position: relative; padding-left: 40px; }
  .address + .address { margin-top: 2px; }
  .address-icon { position: absolute; left: 0; top: 4px; width: 28px; height: 28px; }

  .person {
    position: absolute; left: 0; top: 344px; width: 100%;
    text-align: center;
  }
  .person-name {
    font-size: 54px; font-weight: 400; color: var(--ink); line-height: 1.1;
  }
  .person-role {
    margin-top: 0; font-size: 20px; letter-spacing: 0.06em;
    color: var(--on-teal);
  }

  .contacts {
    position: absolute; left: 36px; right: 36px; top: 478px;
    display: flex; justify-content: space-between; list-style: none;
    color: var(--on-teal); font-size: 22px; white-space: nowrap;
  }
  .contact { display: flex; align-items: center; gap: 10px; }
  .contact-icon { width: 30px; height: 30px; flex: none; }
</style>
</head>
<body>
<main class="stage">
  <article class="business-card">
    <header class="brand">
      <span class="brand-dot"></span>
      <p class="brand-name">MAPLE GROVE FELLOWSHIP</p>
      <p class="brand-tagline">Still waters, open door</p>
    </header>

    <ul class="addresses">
      <li class="address">
        <svg class="address-icon" viewBox="0 0 28 28" aria-hidden="true">
          <circle cx="14" cy="14" r="12.5" fill="none" stroke="#4dbfbd" stroke-width="2"/>
          <path d="M14 6c-3 0-5 2.2-5 5 0 3.6 5 9 5 9s5-5.4 5-9c0-2.8-2-5-5-5z" fill="#4dbfbd"/>
          <circle cx="14" cy="11" r="1.8" fill="#fff"/>
        </svg>
        3-9-4 Kawaranodai, Kaede-ku<br>Tokyo 164-0012 (Church)
      </li>
      <li class="address">
        <svg class="address-icon" viewBox="0 0 28 28" aria-hidden="true">
          <circle cx="14" cy="14" r="12.5" fill="none" stroke="#4dbfbd" stroke-width="2"/>
          <path d="M7 14l7-6 7 6h-2v6h-4v-4h-2v4H9v-6z" fill="#4dbfbd"/>
        </svg>
        2-21 Ochibamachi, Kaede-ku<br>Tokyo 164-0027 (Home)
      </li>
    </ul>

    <div class="divider"></div>
    <section class="card-band"></section>

    <div class="person">
      <h1 class="person-name">Mattias R. Pellworth</h1>
      <p class="person-role">PASTOR</p>
    </div>

    <ul class="contacts">
      <li class="contact">
        <svg class="contact-icon" viewBox="0 0 30 30" aria-hidden="true">
          <circle cx="15" cy="15" r="15" fill="#fff"/>
          <path d="M10.5 8.5l3 3-1.6 1.8c.9 1.9 2.4 3.4 4.3 4.3l1.8-1.6 3 3-1.8 2.2C13.5 21 9 16.5 8.8 10.3z" fill="#5bc5c7"/>
        </svg>
        03-5817-2963
      </li>
      <li class="contact">
        <svg class="contact-icon" viewBox="0 0 30 30" aria-hidden="true">
          <circle cx="15" cy="15" r="15" fill="#fff"/>
          <circle cx="15" cy="15" r="8" fill="none" stroke="#5bc5c7" stroke-width="1.6"/>
          <ellipse cx="15" cy="15" rx="3.5" ry="8" fill="none" stroke="#5bc5c7" stroke-width="1.4"/>
          <path d="M7 15h16" stroke="#5bc5c7" stroke-width="1.4"/>
        </svg>
        www.maplegrovefell.org
      </li>
      <li class="contact">
        <svg class="contact-icon" viewBox="0 0 30 30" aria-hidden="true">
          <circle cx="15" cy="15" r="15" fill="#fff"/>
          <rect x="8" y="10" width="14" height="10" fill="none" stroke="#5bc5c7" stroke-width="1.6"/>
          <path d="M8 10l7 6 7-6" fill="none" stroke="#5bc5c7" stroke-width="1.6"/>
        </svg>
        pastor@maplegrovefell.org
      </li>
    </ul>
  </article>
</main>
</body>
</html>
```